Medical Staffing agency

I need a logo design that can stand along and become a brand. I'm not too particular of the design. Want something catchy and hopefully related to the Health field. Not important though. An example of what I'm looking for is the Stride Forge Logo, or the Vantora Logo. Something that can become a brand without having to say the brand name. A bit about my company, I hire medical staff, and contract with other companies to provide anywhere from short term to long term employees. But that is expanding to more than just that.

Industry/Entity Type

Medical

Contact Information for Business Card

Westmere Rehab Services
Dalen Whitcombe, CEO
742 Brookhollow Ave
Suite 48
Larkmont, CA 95718

```html
<!DOCTYPE html>
<html lang="en">
<head>
<meta charset="UTF-8">
<title>Westmere Rehab Services – Business Cards</title>
<link rel="stylesheet" href="https://fonts.googleapis.com/css2?family=Arimo:wght@400;700&family=Tinos:wght@400;700&display=swap">
<style>
  :root {
    --backdrop: #8e8f91;
    --card: #fbfbfa;
    --navy: #27307a;
    --red: #c8262c;
    --ink: #151515;
    --band: #1c1c1c;
  }
  * { margin: 0; padding: 0; box-sizing: border-box; }
  html, body { width: 1200px; height: 1200px; overflow: hidden; }
  body {
    background: var(--backdrop);
    position: relative;
    font-family: "Arimo", Arial, sans-serif;
  }
  .card {
    position: absolute;
    left: 250px;
    width: 700px;
    height: 400px;
    background: var(--card);
    box-shadow: 0 6px 18px rgba(0,0,0,0.25);
    overflow: hidden;
  }
  .card-front { top: 140px; }
  .card-back { top: 640px; }

  /* Front */
  .brand {
    position: absolute;
    left: 0; right: 0; top: 150px;
    display: flex;
    align-items: center;
    justify-content: center;
    gap: 16px;
  }
  .brand-mark {
    flex: none;
    width: 34px; height: 34px;
    background: var(--red);
  }
  .brand-name {
    color: var(--navy);
    font-weight: 400;
    font-size: 34px;
    letter-spacing: 2px;
    line-height: 1.1;
  }
  .brand-name .brand-sub {
    display: block;
    font-size: 20px;
    letter-spacing: 1px;
    text-align: right;
  }

  /* Back */
  .back-brand {
    position: absolute;
    left: 56px; top: 100px;
    display: flex;
    align-items: center;
    gap: 10px;
  }
  .back-brand .brand-mark { width: 22px; height: 22px; }
  .back-brand .brand-name { font-size: 17px; letter-spacing: 1px; }
  .contact {
    position: absolute;
    left: 300px; top: 74px;
    color: var(--ink);
  }
  .contact-role {
    font-family: "Tinos", "Times New Roman", serif;
    font-size: 16px;
    text-decoration: underline;
  }
  .contact-name {
    font-family: "Tinos", "Times New Roman", serif;
    font-weight: 700;
    font-size: 19px;
    margin-bottom: 6px;
  }
  .contact-address {
    font-size: 20px;
    line-height: 1.15;
  }
  .band {
    position: absolute;
    left: 0; right: 0;
    top: 220px;
    height: 150px;
    background: var(--band);
  }
</style>
</head>
<body>
  <section class="card card-front" aria-label="Business card front">
    <div class="brand">
      <span class="brand-mark"></span>
      <span class="brand-name">WESTMERE REHAB<span class="brand-sub">Services LLC</span></span>
    </div>
  </section>

  <section class="card card-back" aria-label="Business card back">
    <div class="back-brand">
      <span class="brand-mark"></span>
      <span class="brand-name">WESTMERE</span>
    </div>
    <div class="contact">
      <p class="contact-role">CEO</p>
      <p class="contact-name">Dalen Whitcombe</p>
      <p class="contact-address">742 Brookhollow Ave Suite 48 Larkmont<br>CA 95718</p>
    </div>
    <div class="band"></div>
  </section>
</body>
</html>
```